Rocket business card

Modern business card design, use of color is good with clean space too.

Things to include on card:

Quote: I add fuel to your optometry practice

- Eyewear Sales
- Admin Duties
- Revenue Collection
- Leadership
- Tech Adoption
- COGS Reduction
- Product Sourcing
-Medical Growth

Dalton Vessey, CEO
Glint Harbor
Text Me! 847-302-1964
dalton@glintharbor.example

```html
<!DOCTYPE html>
<html lang="en">
<head>
<meta charset="utf-8">
<title>Glint Harbor – Business Card</title>
<link rel="stylesheet" href="https://fonts.googleapis.com/css2?family=Lato:wght@400;700&display=swap">
<style>
  :root {
    --page: #e9e6e1;
    --card-white: #f7f7f7;
    --ink: #111111;
    --black-panel: #0b0b0b;
    --red: #c9412f;
    --orange: #ea7a2a;
    --amber: #f0a526;
    --yellow: #f2c21c;
    --muted-ink: #222222;
    --on-dark: #ffffff;
  }
  * { box-sizing: border-box; margin: 0; padding: 0; }
  html, body { width: 1200px; height: 780px; overflow: hidden; }
  body {
    background: var(--page);
    font-family: "Lato", Arial, sans-serif;
    color: var(--ink);
    position: relative;
  }
  .card {
    position: absolute;
    top: 230px;
    width: 560px;
    height: 320px;
    background: var(--card-white);
    overflow: hidden;
    box-shadow: 0 6px 18px rgba(0,0,0,0.18);
  }
  .card--front { left: 27px; }
  .card--back { left: 613px; }

  .card__art { position: absolute; inset: 0; width: 100%; height: 100%; }

  /* Brand lockup */
  .brand {
    position: absolute;
    display: flex;
    align-items: center;
    gap: 14px;
  }
  .brand__dot {
    width: 44px; height: 44px; border-radius: 50%;
    background: var(--orange);
    flex: none;
  }
  .brand__name {
    font-weight: 400;
    font-size: 30px;
    letter-spacing: 3px;
    text-transform: uppercase;
    color: var(--ink);
    white-space: nowrap;
  }
  .card--front .brand {
    left: 32px; top: 96px;
    flex-direction: column;
    align-items: flex-start;
    gap: 14px;
  }
  .card--front .brand__dot { width: 52px; height: 52px; }
  .card--front .brand__name { font-size: 26px; letter-spacing: 2.5px; }

  /* Contact block */
  .contact {
    position: absolute;
    left: 352px; top: 96px;
    color: var(--on-dark);
  }
  .contact__name {
    font-size: 19px; font-weight: 700;
    letter-spacing: 1px; text-transform: uppercase;
  }
  .contact__title {
    font-size: 15px; color: var(--orange);
    margin: 2px 0 14px 120px; text-transform: uppercase; letter-spacing: 1px;
  }
  .contact__line {
    display: flex; align-items: center; gap: 8px;
    font-size: 13.5px; margin-bottom: 6px; white-space: nowrap;
  }
  .contact__icon {
    width: 16px; height: 16px; border-radius: 4px;
    background: var(--orange); flex: none;
  }

  /* Back */
  .card--back .brand { left: 40px; top: 32px; }
  .card--back .brand__dot { width: 40px; height: 40px; }
  .card--back .brand__name { font-size: 27px; }
  .services {
    position: absolute; left: 40px; top: 134px;
    display: flex; gap: 36px;
  }
  .service-group { list-style: none; }
  .service-group li {
    font-size: 13.5px; color: var(--muted-ink);
    line-height: 19px; display: flex; align-items: center; gap: 7px;
  }
  .service-group li::before {
    content: ""; width: 7px; height: 7px; border-radius: 50%;
    background: var(--orange); flex: none;
  }
</style>
</head>
<body>

  <section class="card card--front" aria-label="Card front">
    <svg class="card__art" viewBox="0 0 560 320" aria-hidden="true">
      <defs>
        <linearGradient id="swoosh" x1="0" y1="1" x2="0" y2="0">
          <stop offset="0" stop-color="var(--red)"/>
          <stop offset="0.5" stop-color="var(--orange)"/>
          <stop offset="1" stop-color="var(--yellow)"/>
        </linearGradient>
      </defs>
      <path d="M300 0 C340 110 320 230 250 320 L560 320 L560 0 Z" fill="url(#swoosh)"/>
      <path d="M306 0 C352 110 340 230 290 320 L560 320 L560 0 Z" fill="var(--black-panel)"/>
    </svg>
    <div class="brand">
      <span class="brand__dot"></span>
      <span class="brand__name">Glint Harbor</span>
    </div>
    <div class="contact">
      <p class="contact__name">Dalton Vessey</p>
      <p class="contact__title">CEO</p>
      <p class="contact__line"><span class="contact__icon"></span>Text Me! 847-302-1964</p>
      <p class="contact__line"><span class="contact__icon"></span>dalton@glintharbor.example</p>
    </div>
  </section>

  <section class="card card--back" aria-label="Card back">
    <svg class="card__art" viewBox="0 0 560 320" aria-hidden="true">
      <defs>
        <linearGradient id="rule" x1="0" y1="0" x2="1" y2="0">
          <stop offset="0" stop-color="var(--red)"/>
          <stop offset="1" stop-color="var(--yellow)"/>
        </linearGradient>
      </defs>
      <circle cx="470" cy="240" r="120" fill="none" stroke="#e6e6e6" stroke-width="10"/>
      <circle cx="470" cy="240" r="88" fill="#f3e6df"/>
      <rect x="40" y="112" width="420" height="2" fill="url(#rule)"/>
      <rect x="0" y="310" width="560" height="10" fill="url(#rule)"/>
    </svg>
    <div class="brand">
      <span class="brand__dot"></span>
      <span class="brand__name">Glint Harbor</span>
    </div>
    <div class="services">
      <ul class="service-group">
        <li>Eyewear Sales</li>
        <li>Admin Duties</li>
        <li>Revenue Collection</li>
      </ul>
      <ul class="service-group">
        <li>Leadership</li>
        <li>Tech Adoption</li>
        <li>COGs Reduction</li>
      </ul>
      <ul class="service-group">
        <li>Product Sourcing</li>
        <li>Medical Growth</li>
      </ul>
    </div>
  </section>

</body>
</html>
```